Business Card for Language School (2 locations)

We need a sleek business card for a language school that is looking to update our image to be more professional. We work with students ages Pre-Kindergarten through adults. Our idea is to have an all-black business card with white or silver lettering. On the front will be the name of our school (Bright Meadow English Academy), and on the back there will be information for our location, phone number, email, and website (and possibly social media information). We have two school branches, so the address, phone number, and email address will be different for each branch, but all of the other information will stay the same. We'd like each branch to have a different color card edge that is neon. We are also open to suggestions and new ideas!

Some answers to questions we have received:
1. The reason we haven't added a logo is because we are looking to get a new one. We hadn't originally planned to do that at this time, but we are going to look into updating our project to include that as another aspect of it. We had previously planned to just include the school name on the front without a logo at this time.
2. We currently have two branches of our school, and we want our business card design to be uniform for each location. While it might make sense to put the information on one card right now, we plan to have more locations in the future, so we want to plan ahead with a unified design right now.
3. Our school addresses and phone numbers can be found on our website: www.brightmeadowlingo.example (at the bottom of the page)!
Updates

Part of this contest is also a new logo design. Our previous design was a train, which we would be open to keeping if it had an updated, sleeker design.

Contact Information for Business Card

Card #1:
Bright Meadow English Academy (Qinglu Branch)
Fuxing W. Rd. Sec. 3, Lane 412, No. 58, 1F
Beitou District, Taipei City 11260
02-2941-3086
qinglu@brightmeadowlingo.example

Card #2:
Bright Meadow English Academy (Heping Branch)
Fuxing W. Rd. Sec. 3, Lane 412, No. 58, 1F
Beitou District, Taipei City 11260
02-2941-3086
qinglu@brightmeadowlingo.example

Both cards:
Website: www.brightmeadowlingo.example
Facebook: www.facebook.com/brightmeadowlingo
Instagram: @brightmeadowlingo

```html
<!DOCTYPE html>
<html lang="en">
<head>
<meta charset="utf-8">
<title>Bright Meadow English Academy – Business Card</title>
<link rel="stylesheet" href="https://fonts.googleapis.com/css2?family=Roboto+Slab:wght@300;700&family=Roboto:wght@300;400&display=swap">
<style>
  :root {
    --backdrop: #dde3ec;
    --card-black: #070304;
    --edge-blue: #188bb8;
    --ink-white: #ffffff;
    --ink-silver: #c9c9c9;
    --ink-grey: #8d8d8d;
    --icon-fill: #b8b8b8;
  }
  * { margin: 0; padding: 0; box-sizing: border-box; }
  html, body {
    width: 1200px; height: 940px; overflow: hidden;
    background: var(--backdrop);
    font-family: "Roboto", Arial, sans-serif;
  }
  .sheet {
    width: 1200px; height: 940px;
    display: flex; flex-direction: column; align-items: center;
    justify-content: center; gap: 40px;
  }
  .card {
    position: relative;
    width: 756px; height: 420px;
    background: var(--card-black);
    overflow: hidden;
    box-shadow: 0 10px 30px rgba(40, 55, 80, 0.18);
  }
  .edge { position: absolute; left: 0; right: 0; height: 32px; background: var(--edge-blue); }
  .edge--top { top: 0; }
  .edge--bottom { bottom: 0; }

  /* Front */
  .front__title {
    position: absolute; left: 0; right: 0; top: 138px;
    text-align: center;
    font-family: "Roboto Slab", Georgia, serif; font-weight: 700;
    font-size: 40px; line-height: 42px; letter-spacing: 0.5px;
    color: var(--ink-white);
  }
  .front__branch {
    position: absolute; left: 0; right: 0; top: 227px;
    text-align: center;
    font-family: "Roboto Slab", Georgia, serif; font-weight: 300;
    font-size: 16px; color: var(--ink-grey);
  }
  .social {
    position: absolute; top: 330px;
    display: flex; align-items: center; gap: 12px;
    font-size: 17px; font-weight: 300; color: var(--ink-silver);
  }
  .social--left { left: 137px; }
  .social--right { left: 438px; }
  .social__dot { width: 16px; height: 16px; border-radius: 50%; background: var(--icon-fill); }

  /* Back */
  .back__name {
    position: absolute; left: 48px; top: 94px;
    font-family: "Roboto Slab", Georgia, serif; font-weight: 700;
    font-size: 21px; line-height: 24px; color: var(--ink-white);
  }
  .back__divider {
    position: absolute; left: 350px; top: 55px; width: 2px; height: 296px;
    background: var(--ink-silver);
  }
  .contact {
    position: absolute; display: flex; align-items: flex-start; gap: 20px;
    font-size: 16px; font-weight: 300; line-height: 20px; color: var(--ink-white);
    white-space: nowrap;
  }
  .contact svg { flex: none; width: 26px; height: 26px; }
  .contact--address { left: 44px; top: 240px; }
  .contact--phone { left: 392px; top: 130px; align-items: center; }
  .contact--email { left: 392px; top: 198px; align-items: center; }
  .contact--web { left: 392px; top: 264px; align-items: center; }
</style>
</head>
<body>
<main class="sheet">

  <section class="card card--front" aria-label="Card front, Qinglu Branch">
    <div class="edge edge--top"></div>
    <h1 class="front__title">BRIGHT MEADOW<br>ENGLISH ACADEMY</h1>
    <p class="front__branch">QINGLU BRANCH</p>
    <div class="social social--left"><span class="social__dot"></span><span>@brightmeadowlingo</span></div>
    <div class="social social--right"><span class="social__dot"></span><span>@brightmeadowlingo</span></div>
    <div class="edge edge--bottom"></div>
  </section>

  <section class="card card--back" aria-label="Card back, Qinglu Branch">
    <h2 class="back__name">BRIGHT MEADOW<br>ENGLISH ACADEMY</h2>
    <div class="back__divider"></div>

    <div class="contact contact--address">
      <svg viewBox="0 0 26 26" aria-hidden="true">
        <circle cx="13" cy="13" r="13" fill="var(--icon-fill)"/>
        <path d="M13 6.5a4.6 4.6 0 0 0-4.6 4.6c0 3.4 4.6 8.4 4.6 8.4s4.6-5 4.6-8.4A4.6 4.6 0 0 0 13 6.5z" fill="var(--card-black)"/>
        <circle cx="13" cy="11.1" r="1.7" fill="var(--icon-fill)"/>
      </svg>
      <p>Fuxing W. Rd. Sec. 3,<br>Lane 412, No. 58, 1F<br>Beitou District,<br>Taipei City 11260</p>
    </div>

    <div class="contact contact--phone">
      <svg viewBox="0 0 26 26" aria-hidden="true">
        <circle cx="13" cy="13" r="13" fill="var(--icon-fill)"/>
        <path d="M9.2 7.2l2 .1 1 2.8-1.4 1.2a7.5 7.5 0 0 0 3.9 3.9l1.2-1.4 2.8 1v2c0 .7-.6 1.2-1.3 1.2A10.6 10.6 0 0 1 8 8.5c0-.7.5-1.3 1.2-1.3z" fill="var(--card-black)"/>
      </svg>
      <span>02-2941-3086</span>
    </div>

    <div class="contact contact--email">
      <svg viewBox="0 0 26 26" aria-hidden="true">
        <circle cx="13" cy="13" r="13" fill="var(--icon-fill)"/>
        <rect x="7.5" y="9" width="11" height="8" rx="1" fill="var(--card-black)"/>
        <path d="M7.8 9.5l5.2 4 5.2-4" fill="none" stroke="var(--icon-fill)" stroke-width="1"/>
      </svg>
      <span>qinglu@brightmeadowlingo.example</span>
    </div>

    <div class="contact contact--web">
      <svg viewBox="0 0 26 26" aria-hidden="true">
        <circle cx="13" cy="13" r="13" fill="var(--icon-fill)"/>
        <g fill="none" stroke="var(--card-black)" stroke-width="1.1">
          <circle cx="13" cy="13" r="6"/>
          <ellipse cx="13" cy="13" rx="2.6" ry="6"/>
          <path d="M7 13h12M8 10h10M8 16h10"/>
        </g>
      </svg>
      <span>www.brightmeadowlingo.example</span>
    </div>

    <div class="edge edge--bottom"></div>
  </section>

</main>
</body>
</html>
```